Information Technology Cloud Services Website

"Offer in every submission a high resolution version of your concept please. It is difficult to see of my text (sales copy) was added to your screenshot or not. It is necessary for me to provide high quality feedback."

My company provides a customizable ecosystem for Trelvane Workdesk 720 and Kolbrin users that includes all the technologies for organizing business processes and communications, letting my clients manage business without fear.

You can see our current site at http://www.720ShiftSpecialists.com

I currently use WordPress using the theme platform OptimizePress. If you have OptimizePress, that would be perfect, yet not required. However, I do need the finish product in WordPress for future additions and edits.

The Brand colors are Light Blue just like the logo attached.

I am in the need of graphic images on every webpage that can convey the services that my company does.

We need a refresh of our existing website that looks more 2018. We have made a mockup of the content that we want and a sample of where we want it. Nothing is set in stone, if you have better ideas of where things should go, feel free.

My instructions are inside the Word document named File 8: 720 Homepage Layout Monday, 22 January 2018 08:06:03

Here are some competitors similar sites we like - but still looking for a unique design that fits out brand

https://www.brovantech.com/

https://www.quorlymail.com/email-migrations/workdesk-720-shift-specialists

https://www.zendrofal.com/solutions/mailbox-migration/

https://www.plumacore.com/

https://www.plumacore.com/workdesk-720/

Target Market(s)

Business = IT Managers, IT Directors, IT Staff, IT Vice Presidents, Chief Information Officer

Industry/Entity Type

Information Technology

Coding

Coded - Design and coding required

Number of Pages Required

5+ page

Font styles to use
Sans Serif

Colors

Designer to choose colors to be used in the design.

Requirements
Must have
• Must have creative graphic images that convey the story/services that I offer. Its important to us that the design is very explanatory, the customer should easily be able to figure out that we provide Workdesk 720 migrations services right away. Also we are looking for a new very responsive HTML5+ webpages in WordPress.

```html
<!DOCTYPE html>
<html lang="en">
<head>
<meta charset="utf-8">
<title>720ShiftSpecialists – Home</title>
<link rel="stylesheet" href="https://fonts.googleapis.com/css2?family=Poppins:wght@300;400;500;600;700&display=swap">
<style>
  :root{
    --blue:#1e8cee;
    --blue-deep:#1578d6;
    --sky:#1aa8f0;
    --navy:#0b2c50;
    --navy-2:#0f3560;
    --ink:#1d2a3a;
    --body:#4a5563;
    --accent:#1e8cee;
    --grey-bg:#f3f2f4;
    --cta-bg:#66b9f6;
    --white:#ffffff;
  }
  *{margin:0;padding:0;box-sizing:border-box}
  html,body{width:1200px;height:2214px;overflow:hidden}
  body{position:relative;font-family:"Poppins",sans-serif;color:var(--ink);background:var(--white)}
  .abs{position:absolute}

  /* top bar */
  .topbar{left:0;top:0;width:1200px;height:32px;background:var(--blue)}
  .topbar .phone{position:absolute;left:925px;top:6px;color:#fff;font-size:15px;font-weight:300;display:flex;align-items:center;gap:8px}

  /* header */
  .brand{left:0;top:32px;width:372px;height:54px;background:var(--navy);display:flex;align-items:center;padding-left:186px;gap:8px}
  .brand .mark{width:26px;height:26px;border:2px solid #fff;border-radius:50%}
  .brand .name{color:#fff;font-size:11px;font-weight:600;letter-spacing:.2px}
  .nav{left:391px;top:32px;width:809px;height:54px;background:#fff;display:flex;align-items:center;box-shadow:0 2px 4px rgba(0,0,0,.08)}
  .nav a{position:absolute;top:18px;font-size:13.5px;color:var(--ink);text-decoration:none;font-weight:400}
  .nav a.active{font-weight:600}
  .nav a.active::before{content:"";position:absolute;left:-6px;right:-6px;top:-18px;height:3px;background:var(--navy)}
  .nav a.active::after{content:"";position:absolute;left:-6px;right:-6px;bottom:-20px;height:3px;background:var(--navy)}
  .nav .search{position:absolute;left:772px;top:0;width:37px;height:54px;background:#eef1f5;display:flex;align-items:center;justify-content:center}

  /* hero */
  .hero{left:0;top:86px;width:1200px;height:512px;background:var(--blue)}
  .hero-stripe{left:0;top:590px;width:1200px;height:8px;background:#b9dcfb}
  .hero-art{left:44px;top:155px;width:480px;height:435px;border-radius:6px;background:linear-gradient(160deg,#3aa2f2 0%,#2893ee 55%,#1c86e4 100%)}
  .hero-title{left:611px;top:194px;width:420px;color:#fff;font-size:19px;font-weight:600;line-height:27px;text-transform:uppercase}
  .hero-sub{left:611px;top:296px;width:300px;color:#e6f2ff;font-size:11.5px;font-weight:300;line-height:19px}
  .btn{display:flex;align-items:center;justify-content:center;gap:8px;height:33px;border-radius:17px;color:#fff;font-size:11.5px;font-weight:400}
  .btn-quote{left:611px;top:365px;width:142px;background:var(--sky);box-shadow:0 3px 8px rgba(0,40,90,.25)}
  .btn-more{left:763px;top:365px;width:142px;background:var(--navy-2);box-shadow:0 3px 8px rgba(0,40,90,.25)}
  .slider-arrows{left:546px;top:552px}

  /* press band */
  .press{left:0;top:598px;width:1200px;height:105px;background:var(--navy)}
  .press .label{position:absolute;left:174px;top:42px;color:#fff;font-size:16px;font-weight:400}
  .press .outlet{position:absolute;top:34px;color:#fff;font-size:28px;font-weight:700;letter-spacing:.5px}

  /* about */
  .about-art{left:171px;top:785px;width:418px;height:417px;background:linear-gradient(135deg,#e4e9ef 0%,#cfd8e2 50%,#e8ecf1 100%)}
  .about-art .focus{position:absolute;left:86px;top:74px;width:246px;height:245px;background:linear-gradient(135deg,#c9b7a6 0%,#8f9aa8 55%,#5c6e84 100%);box-shadow:0 6px 18px rgba(0,0,0,.15)}
  .about-copy{left:611px;top:780px;width:420px;font-size:11.3px;line-height:22.3px;color:var(--body);font-weight:300}
  .about-copy p{margin-bottom:8px}
  .about-copy h3{font-size:14.5px;font-weight:500;color:var(--ink);margin:4px 0 8px}
  .about-copy .lead{font-weight:500;color:var(--navy)}
  .about-copy .lead.blue{color:var(--accent)}

  /* process */
  .process{left:0;top:1287px;width:1200px;height:636px;background:var(--grey-bg)}
  .process-title{left:0;top:1335px;width:1200px;text-align:center;font-size:40px;font-weight:500;color:var(--navy);letter-spacing:1px}
  .process-title span{color:var(--accent)}
  .process-sub{left:0;top:1400px;width:1200px;text-align:center;font-size:15px;font-weight:300;color:#3b4656;letter-spacing:.3px}
  .step-card-text{left:181px;top:1690px;width:140px;text-align:center;color:#fff;font-size:9.6px;line-height:15px;font-weight:300}

  /* call to action */
  .cta{left:0;top:1923px;width:1200px;height:291px;background:var(--cta-bg)}
  .cta-art{left:694px;top:1931px;width:506px;height:283px;border-radius:4px 0 0 0;background:linear-gradient(150deg,#8ccaf8 0%,#3f8fd6 55%,#1e4f86 100%)}
  .cta-text{left:173px;top:1972px;width:520px;color:#fff;font-size:20px;font-weight:300;line-height:31.5px}
  .btn-cta{left:173px;top:2133px;width:188px;height:32px;background:var(--navy);font-size:12px}
</style>
</head>
<body>

  <div class="abs topbar">
    <div class="phone">
      <svg width="15" height="15" viewBox="0 0 24 24" fill="none" stroke="#fff" stroke-width="1.8"><path d="M5 3h4l2 5-2.5 1.5a11 11 0 0 0 6 6L16 13l5 2v4a2 2 0 0 1-2 2A17 17 0 0 1 3 5a2 2 0 0 1 2-2z"/></svg>
      Call us: (800) 555-0147
    </div>
  </div>

  <div class="abs brand">
    <span class="mark"></span>
    <span class="name">720ShiftSpecialists.com</span>
  </div>

  <nav class="abs nav">
    <a class="active" style="left:30px">Home</a>
    <a style="left:106px">Email Migrations</a>
    <a style="left:249px">Migration Solutions</a>
    <a style="left:407px">Mergers</a>
    <a style="left:497px">Technology Services</a>
    <a style="left:668px">About Us</a>
    <div class="search">
      <svg width="20" height="20" viewBox="0 0 24 24" fill="none" stroke="#1d2a3a" stroke-width="1.8"><circle cx="10" cy="10" r="7"/><path d="M15 15l7 7"/></svg>
    </div>
  </nav>

  <section class="abs hero"></section>
  <div class="abs hero-stripe"></div>
  <div class="abs hero-art" role="img" aria-label="Illustration of an IT specialist at a desk with floating code windows"></div>
  <h1 class="abs hero-title">Are you willing to cut costs &amp; boost productivity by migrating your email server &amp;infrastructure to the cloud?</h1>
  <p class="abs hero-sub">We Help Companies Quickly and Professionally Migrate To Workdesk 720 &amp; Kolbrin</p>
  <a class="abs btn btn-quote">Request a Quote
    <svg width="14" height="10" viewBox="0 0 14 10" fill="none" stroke="#fff" stroke-width="1.4"><path d="M0 5h12M8 1l4 4-4 4"/></svg></a>
  <a class="abs btn btn-more">Learn More
    <svg width="14" height="10" viewBox="0 0 14 10" fill="none" stroke="#fff" stroke-width="1.4"><path d="M0 5h12M8 1l4 4-4 4"/></svg></a>
  <svg class="abs slider-arrows" width="92" height="24" viewBox="0 0 92 24" fill="none" stroke-width="1.6">
    <path d="M42 12H4M11 5l-7 7 7 7" stroke="#0b2c50"/>
    <path d="M68 12h20M81 5l7 7-7 7" stroke="#fff"/>
  </svg>

  <section class="abs press">
    <span class="label">As Seen In:</span>
    <span class="outlet" style="left:328px">Vantor</span>
    <span class="outlet" style="left:472px">Pellcast</span>
    <span class="outlet" style="left:657px">Orbis News</span>
    <span class="outlet" style="left:860px">Kestrel</span>
  </section>

  <div class="abs about-art" role="img" aria-label="Photo collage of a team working together at a computer">
    <div class="focus"></div>
  </div>
  <div class="abs about-copy">
    <p>When it comes to migrating your email server, apps or infrastructure to the cloud, you don't have to lose sleep or spend over your budget. All you have to do is choose 720ShiftSpecialists and we will professionally and efficiently handle every single detail.</p>
    <h3>Here's How 720ShiftSpecialists Can Help Your Business</h3>
    <p><span class="lead">SAVE TIME–</span> Our team of experts will determine your needs and develop a 100% custom migration strategy tailored to your company. We will analyze your current environment and prepare your Workdesk 720 profiles and users. You do not have to trouble yourself with all the technical details anymore.</p>
    <p><span class="lead blue">SAVE EFFORT–</span> After identifying your needs, we will start migrating your data. Your email service will be re-routed to Workdesk 720 and we will help you set up the new email service on all your local desktops and mobile devices. Once the migration process is complete, we will review the results and ensure that everything went according to plan.</p>
    <p><span class="lead blue">SAVE MONEY–</span> Migrating your data to Workdesk 720 means cutting down on expenses and boosting your performance. Plus, we offer you flexible monthly licenses, so you are not stuck with upfront annual contract license costs.</p>
  </div>

  <section class="abs process"></section>
  <h2 class="abs process-title">OUR <span>MIGRATION</span> PROCESS</h2>
  <p class="abs process-sub">AT ANY TIME OF THE DAY OR NIGHT, 24/7 &amp; 365 DAYS OUT OF THE YEAR</p>

  <svg class="abs" style="left:0;top:1287px" width="1200" height="636" viewBox="0 1287 1200 636" font-family="Poppins, sans-serif">
    <defs>
      <marker id="arrowhead" markerWidth="10" markerHeight="10" refX="5" refY="5" orient="auto">
        <path d="M0 1l8 4-8 4z" fill="#0b2c50"/>
      </marker>
    </defs>
    <g fill="none" stroke="#0b2c50" stroke-width="2.4" marker-end="url(#arrowhead)">
      <path d="M252 1538C262 1462 405 1458 422 1534"/>
      <path d="M427 1538C437 1462 580 1458 594 1534"/>
      <path d="M599 1538C609 1462 752 1458 767 1534"/>
      <path d="M772 1538C782 1462 932 1458 947 1534"/>
    </g>

    <!-- first contact card -->
    <rect x="173" y="1628" width="157" height="217" fill="#0b2c50"/>

    <g id="steps">
      <!-- step: cx, fill -->
      <g>
        <circle cx="252" cy="1628" r="78" fill="#0b2c50"/>
        <path d="M191 1580A78 78 0 0 1 313 1580Z" fill="#f3f2f4"/>
        <path d="M190 1568A88 88 0 0 1 314 1568" fill="none" stroke="#1e8cee" stroke-width="3"/>
        <circle cx="252" cy="1540" r="4" fill="#fff" stroke="#1e8cee" stroke-width="2"/>
        <circle cx="252" cy="1628" r="40" fill="#fff"/>
        <circle cx="252" cy="1628" r="32" fill="none" stroke="#0b2c50" stroke-width="2"/>
        <text x="252" y="1559" font-size="13.5" fill="#1d2a3a" text-anchor="middle">First</text>
        <text x="252" y="1576" font-size="13.5" fill="#1d2a3a" text-anchor="middle">Contact</text>
        <g fill="none" stroke="#0b2c50" stroke-width="1.6"><rect x="238" y="1618" width="28" height="19"/><path d="M238 1618l14 11 14-11"/></g>
      </g>
      <g>
        <circle cx="427" cy="1628" r="78" fill="#1e8cee"/>
        <path d="M366 1580A78 78 0 0 1 488 1580Z" fill="#f3f2f4"/>
        <path d="M365 1568A88 88 0 0 1 489 1568" fill="none" stroke="#1e8cee" stroke-width="3"/>
        <circle cx="427" cy="1540" r="4" fill="#fff" stroke="#1e8cee" stroke-width="2"/>
        <circle cx="427" cy="1628" r="40" fill="#fff"/>
        <circle cx="427" cy="1628" r="32" fill="none" stroke="#0b2c50" stroke-width="2"/>
        <text x="427" y="1559" font-size="13.5" fill="#1d2a3a" text-anchor="middle">Pre</text>
        <text x="427" y="1576" font-size="13.5" fill="#1d2a3a" text-anchor="middle">Migration</text>
        <g fill="none" stroke="#0b2c50" stroke-width="1.6"><path d="M415 1628a8 8 0 0 1 3-15 10 10 0 0 1 19 2 7 7 0 0 1 1 13z"/><rect x="420" y="1632" width="14" height="10"/></g>
      </g>
      <g>
        <circle cx="599" cy="1628" r="78" fill="#0b2c50"/>
        <path d="M538 1580A78 78 0 0 1 660 1580Z" fill="#f3f2f4"/>
        <path d="M537 1568A88 88 0 0 1 661 1568" fill="none" stroke="#1e8cee" stroke-width="3"/>
        <circle cx="599" cy="1540" r="4" fill="#fff" stroke="#1e8cee" stroke-width="2"/>
        <circle cx="599" cy="1628" r="40" fill="#fff"/>
        <circle cx="599" cy="1628" r="32" fill="none" stroke="#0b2c50" stroke-width="2"/>
        <text x="599" y="1559" font-size="13.5" fill="#1d2a3a" text-anchor="middle">Start</text>
        <text x="599" y="1576" font-size="13.5" fill="#1d2a3a" text-anchor="middle">Migration</text>
        <g fill="none" stroke="#0b2c50" stroke-width="1.6"><rect x="585" y="1614" width="28" height="9"/><rect x="585" y="1623" width="28" height="9"/><rect x="585" y="1632" width="28" height="9"/><path d="M605 1629v-6m-3 3l3-3 3 3"/></g>
      </g>
      <g>
        <circle cx="772" cy="1628" r="78" fill="#1e8cee"/>
        <path d="M711 1580A78 78 0 0 1 833 1580Z" fill="#f3f2f4"/>
        <path d="M710 1568A88 88 0 0 1 834 1568" fill="none" stroke="#1e8cee" stroke-width="3"/>
        <circle cx="772" cy="1540" r="4" fill="#fff" stroke="#1e8cee" stroke-width="2"/>
        <circle cx="772" cy="1628" r="40" fill="#fff"/>
        <circle cx="772" cy="1628" r="32" fill="none" stroke="#0b2c50" stroke-width="2"/>
        <text x="772" y="1559" font-size="13.5" fill="#1d2a3a" text-anchor="middle">Local</text>
        <text x="772" y="1576" font-size="13.5" fill="#1d2a3a" text-anchor="middle">Setup</text>
        <g fill="none" stroke="#0b2c50" stroke-width="1.6"><rect x="764" y="1610" width="16" height="22"/><path d="M767 1616h10M767 1621h10M772 1632v8M760 1642h24"/></g>
      </g>
      <g>
        <circle cx="952" cy="1628" r="78" fill="#0b2c50"/>
        <path d="M891 1580A78 78 0 0 1 1013 1580Z" fill="#f3f2f4"/>
        <path d="M890 1568A88 88 0 0 1 1014 1568" fill="none" stroke="#1e8cee" stroke-width="3"/>
        <circle cx="952" cy="1540" r="4" fill="#fff" stroke="#1e8cee" stroke-width="2"/>
        <circle cx="952" cy="1628" r="40" fill="#fff"/>
        <circle cx="952" cy="1628" r="32" fill="none" stroke="#0b2c50" stroke-width="2"/>
        <text x="952" y="1559" font-size="13.5" fill="#1d2a3a" text-anchor="middle">Post</text>
        <text x="952" y="1576" font-size="13.5" fill="#1d2a3a" text-anchor="middle">Migration</text>
        <g fill="none" stroke="#0b2c50" stroke-width="1.6"><rect x="940" y="1612" width="22" height="28"/><path d="M945 1620h12M945 1626h12M945 1632h8"/><path d="M958 1614a6 6 0 0 1 8 6h-8z"/></g>
      </g>
    </g>
  </svg>
  <p class="abs step-card-text">Our team of Experts will contact you to determine your needs and develop a custom migration strategy. A dedicated migration agent will be assigned to your account as the main contact for the whole migration process.</p>

  <section class="abs cta"></section>
  <div class="abs cta-art" role="img" aria-label="Illustration of hands working at a laptop and keyboard with code on screen"></div>
  <p class="abs cta-text">Cloud Services Like Trelvane Workdesk 720 And Kolbrin Can Help You Boost Your Productivity? Speak With One Of Our Expert Engineers About Your Business Goals</p>
  <a class="abs btn btn-cta">Request a Quote Today!
    <svg width="14" height="10" viewBox="0 0 14 10" fill="none" stroke="#fff" stroke-width="1.4"><path d="M0 5h12M8 1l4 4-4 4"/></svg></a>

</body>
</html>
```